WordPress Website for Accounting Firm

I have attached an excel sheet showing what i need done for my accounting website. Currently i have a WP website but its not live and do not like it. I can give a link if that will help. Total pages is around 12. I can buy and supply the images but have provided indication of what i want in the excel. I will need the designer to do the coding to make the website fully functional. I want a clean look and attractive. Don't want too dark colors. Once i like the landing page, i will need the designer to code code the website. Just want to look first. I will provide the logo file and put the contents myself. Just put dummy contents for now to show how it will look.
Updates
Can you please use the attached images so i can see how nit will look on the coverage as an option. These are from pixelharbor
264918053
418273596
1537206419
1096382147
Currently there are only 2 provided by myself as Photo 1 and Photo 2
Many Thanks!
Industry/Entity Type
Accounting and Finance
Number of Pages Required
5+ page

```html
<!DOCTYPE html>
<html lang="en">
<head>
<meta charset="utf-8">
<title>Ledgerline Tax Advisory</title>
<link href="https://fonts.googleapis.com/css2?family=Poppins:wght@400;500;600;700&display=swap" rel="stylesheet">
<style>
:root{
  --green:#22b07d;
  --green-dark:#178a60;
  --green-soft:#d9f1e7;
  --ink:#1d2a26;
  --text:#4f5a57;
  --nav:#24332e;
  --grey:#eef1f0;
  --footer-a:#1f9b6b;
  --footer-b:#5cbb5f;
  --copy:#17231f;
}
*{margin:0;padding:0;box-sizing:border-box}
html,body{width:1200px;height:3744px;overflow:hidden}
body{font-family:"Poppins",sans-serif;color:var(--text);background:#fff;position:relative}
.abs{position:absolute}
.btn{display:inline-block;background:var(--green);color:#fff;font-weight:500;font-size:14px;padding:11px 24px;border-radius:3px}

/* header */
.topbar{top:0;left:0;width:1200px;height:88px;background:#fff}
.brand{left:34px;top:20px;display:flex;align-items:center;gap:12px}
.brand-dot{width:46px;height:46px;border-radius:50%;background:var(--green)}
.brand-name{font-weight:600;font-size:15px;color:var(--ink);letter-spacing:.5px;line-height:1.2}
.contact-chip{display:flex;align-items:center;gap:10px;top:22px}
.chip-icon{width:36px;height:36px;border-radius:50%;background:var(--green);display:flex;align-items:center;justify-content:center}
.chip-text{font-size:11px;line-height:1.4;color:var(--ink)}
.chip-text b{display:block;color:var(--green);font-weight:500}
.badge{top:22px;width:44px;height:44px;border-radius:50%}

.mainnav{top:88px;left:0;width:1200px;height:44px;background:var(--nav);display:flex;align-items:center;padding-left:60px;z-index:5}
.mainnav a{display:block;color:#fff;font-size:13px;text-decoration:none;padding:0 34px;height:44px;line-height:44px;white-space:nowrap}
.mainnav a.active{background:var(--green);padding:0 54px}
.mainnav .enquire{position:absolute;right:86px;top:6px;height:32px;line-height:32px;background:var(--green);padding:0 20px;border-radius:2px}

/* hero */
.hero{top:132px;left:0;width:1200px;height:460px;background:linear-gradient(90deg,#f4f6f6 0%,#e7ecee 38%,#c9d2d8 60%,#aebac3 100%)}
.hero-photo{top:132px;left:360px;width:840px;height:460px;background:linear-gradient(120deg,rgba(255,255,255,0) 0%,rgba(120,140,155,.35) 60%,rgba(70,85,100,.45) 100%)}
.hero-copy{left:70px;top:212px;z-index:2}
.hero-copy h1{font-size:58px;line-height:1.08;color:var(--ink);font-weight:700}
.hero-copy h1 span{color:var(--green)}
.hero-copy p{font-size:21px;color:var(--ink);font-weight:500;line-height:1.4;margin:20px 0 30px;width:380px}
.arrow{width:34px;height:34px;display:flex;align-items:center;justify-content:center}

/* about */
.about-mark{left:90px;top:660px;width:380px;height:380px;border-radius:50%;background:radial-gradient(circle at 40% 40%,#ffffff 0%,#eef2f1 55%,#dfe6e4 100%)}
.about-copy{left:690px;top:770px;width:450px}
h2{font-size:32px;font-weight:700;color:var(--ink);margin-bottom:18px}
.about-copy p{font-size:13px;line-height:1.75;margin-bottom:26px}

/* why */
.why{left:70px;top:1210px;width:540px}
.why ul{list-style:none;margin-top:10px}
.why li{display:flex;gap:12px;font-size:13px;line-height:1.5;color:var(--ink);margin-bottom:14px}
.why li svg{flex:0 0 16px;margin-top:2px}
.why-shape{left:700px;top:1230px;width:500px;height:560px;background:var(--green);border-radius:280px 0 0 280px}
.why-photo{left:640px;top:1200px;width:560px;height:590px;border-radius:0 0 0 260px;background:linear-gradient(135deg,#e9e6df 0%,#d8d2c5 45%,#b9b1a2 100%)}

/* testimonials */
.reviews{top:2030px;left:0;width:1200px;height:610px;background:var(--grey)}
.hand{left:360px;top:1975px;width:130px;height:180px;border-radius:60px 60px 20px 20px;background:linear-gradient(180deg,#f2d8c4,#d9b59a)}
.reviews-title{left:500px;top:2075px;font-size:32px;font-weight:700;color:var(--ink);line-height:1.15;text-align:center}
.reviews-title span{color:var(--green)}
.review{top:2300px;width:300px;height:270px;background:#fff;text-align:center;padding:100px 30px 0}
.avatar{position:absolute;top:-60px;left:90px;width:120px;height:120px;border-radius:50%;background:linear-gradient(160deg,#7b746d,#2f2a26);border:5px solid #fff}
.review p{font-size:13px;line-height:1.5;color:var(--ink)}
.review .who{margin-top:14px;font-size:12px;color:var(--text)}
.quote{position:absolute;width:34px;height:34px;border-radius:50%;background:var(--green);color:#fff;font-weight:700;font-size:22px;line-height:40px;text-align:center}

/* industries */
.ind-title{top:2660px;left:0;width:1200px;text-align:center;font-size:34px}
.ind{top:2730px;width:300px}
.ind .num{font-size:120px;font-weight:700;color:#c8ece0;line-height:1}
.ind .pic{margin-top:-60px;height:180px;width:300px}
.ind h3{font-size:17px;font-weight:600;color:var(--ink);margin:22px 0 12px}
.ind p{font-size:13px;line-height:1.6}
.pager{top:3156px;left:540px;display:flex;gap:14px;align-items:center}
.pager span{width:22px;height:22px;border-radius:50%;font-size:11px;text-align:center;line-height:22px;color:var(--ink)}
.pager .on{background:var(--green);color:#fff}

/* footer */
.footer{top:3220px;left:0;width:1200px;height:470px;background:linear-gradient(120deg,var(--footer-a),var(--footer-b))}
.footer *{color:#fff}
.f-brand{left:70px;top:80px;display:flex;align-items:center;gap:12px}
.f-brand .brand-dot{background:#fff}
.f-about{left:70px;top:170px;width:260px;font-size:13px;line-height:1.65}
.f-social{left:70px;top:340px;width:40px;height:40px;border-radius:50%;background:#fff}
.f-col h4{font-size:16px;font-weight:600;margin-bottom:22px}
.f-col li{list-style:none;font-size:13px;margin-bottom:12px;display:flex;align-items:center;gap:10px}
.f-ico{width:22px;height:22px;border-radius:50%;background:rgba(255,255,255,.25);flex:0 0 22px}
.bullet{width:8px;height:8px;border-radius:50%;background:#fff;flex:0 0 8px}
.copy{top:3690px;left:0;width:1200px;height:54px;background:var(--copy);color:#cfd6d3;font-size:13px;text-align:center;line-height:54px}
.to-top{right:50px;top:3697px;width:40px;height:40px;border-radius:50%;background:var(--green);display:flex;align-items:center;justify-content:center}
</style>
</head>
<body>

<header>
  <div class="abs topbar"></div>
  <div class="abs brand"><div class="brand-dot"></div><div class="brand-name">LEDGERLINE<br>TAX ADVISORY</div></div>
  <div class="abs contact-chip" style="left:610px">
    <div class="chip-icon"><svg width="16" height="16" viewBox="0 0 24 24"><path fill="#fff" d="M6.6 10.8a15 15 0 0 0 6.6 6.6l2.2-2.2c.3-.3.7-.4 1-.2 1.1.4 2.3.6 3.6.6.6 0 1 .4 1 1V20c0 .6-.4 1-1 1A17 17 0 0 1 3 4c0-.6.4-1 1-1h3.5c.6 0 1 .4 1 1 0 1.3.2 2.5.6 3.6.1.3 0 .7-.2 1z"/></svg></div>
    <div class="chip-text"><b>Call Us</b>+64 9 555 0142</div>
  </div>
  <div class="abs contact-chip" style="left:820px">
    <div class="chip-icon"><svg width="16" height="16" viewBox="0 0 24 24"><path fill="#fff" d="M3 5h18v14H3zm2 2v.5l7 4.5 7-4.5V7z"/></svg></div>
    <div class="chip-text"><b>Send Enquiry</b>hello@ledgerlinetax.example</div>
  </div>
  <div class="abs badge" style="left:1068px;background:#29a9d8"></div>
  <div class="abs badge" style="left:1120px;background:#7b3a8f"></div>

  <nav class="abs mainnav">
    <a class="active">Home</a><a>Solution ▾</a><a>Clients ▾</a><a>Client Resources ▾</a><a>Contact Us</a>
    <a class="enquire">Enquiry Now</a>
  </nav>
</header>

<section>
  <div class="abs hero" role="img" aria-label="Accountants in suits reviewing figures on a laptop in a bright office"></div>
  <div class="abs hero-photo"></div>
  <div class="abs hero-copy">
    <h1>We are<br>Accounting<br><span>Experts</span></h1>
    <p>We devoted to helping you improve your financial health</p>
    <span class="btn">Contact Us</span>
  </div>
  <div class="abs arrow" style="left:14px;top:374px"><svg width="18" height="28" viewBox="0 0 18 28"><path d="M15 2 3 14l12 12" fill="none" stroke="#1d2a26" stroke-width="4"/></svg></div>
  <div class="abs arrow" style="left:1152px;top:374px"><svg width="18" height="28" viewBox="0 0 18 28"><path d="M3 2l12 12L3 26" fill="none" stroke="#1d2a26" stroke-width="4"/></svg></div>
</section>

<section>
  <div class="abs about-mark" role="img" aria-label="Large brand emblem on a soft circle"></div>
  <div class="abs about-copy">
    <h2>About Us</h2>
    <p>There are many variations of passages of Lorem Ipsum available, but the majority have suffered alteration in some form, by injected humour, or randomised words which don't look even slightly believable. If you are going to use a passage of Lorem Ipsum, you need to be sure there isn't anything embarrassing hidden in the middle of text.</p>
    <span class="btn">Read More</span>
  </div>
</section>

<section>
  <div class="abs why">
    <h2>Why Choose Us</h2>
    <ul>
      <li><svg width="16" height="16" viewBox="0 0 16 16"><path d="M2 8.5l4 4 8-9" fill="none" stroke="#22b07d" stroke-width="2.4"/></svg>Our team are qualified professionals with 50+ years of combined experience in CA industry</li>
      <li><svg width="16" height="16" viewBox="0 0 16 16"><path d="M2 8.5l4 4 8-9" fill="none" stroke="#22b07d" stroke-width="2.4"/></svg>Our team are qualified professionals with 50+ years of combined experience in CA industry</li>
      <li><svg width="16" height="16" viewBox="0 0 16 16"><path d="M2 8.5l4 4 8-9" fill="none" stroke="#22b07d" stroke-width="2.4"/></svg>We are Accessible 7 days a week</li>
      <li><svg width="16" height="16" viewBox="0 0 16 16"><path d="M2 8.5l4 4 8-9" fill="none" stroke="#22b07d" stroke-width="2.4"/></svg>We constantly update to keep up with changes to tax laws and legislation</li>
      <li><svg width="16" height="16" viewBox="0 0 16 16"><path d="M2 8.5l4 4 8-9" fill="none" stroke="#22b07d" stroke-width="2.4"/></svg>Our advise is explained in plain english so you understand</li>
      <li><svg width="16" height="16" viewBox="0 0 16 16"><path d="M2 8.5l4 4 8-9" fill="none" stroke="#22b07d" stroke-width="2.4"/></svg>Our fees are not only fair but very competitive</li>
      <li><svg width="16" height="16" viewBox="0 0 16 16"><path d="M2 8.5l4 4 8-9" fill="none" stroke="#22b07d" stroke-width="2.4"/></svg>We don't believe in one size fits all, we listen to client's challenges individually</li>
      <li><svg width="16" height="16" viewBox="0 0 16 16"><path d="M2 8.5l4 4 8-9" fill="none" stroke="#22b07d" stroke-width="2.4"/></svg>Our level of service and work ethics is no different to any other large CA practices</li>
      <li><svg width="16" height="16" viewBox="0 0 16 16"><path d="M2 8.5l4 4 8-9" fill="none" stroke="#22b07d" stroke-width="2.4"/></svg>We have affiliations with other business partners</li>
      <li><svg width="16" height="16" viewBox="0 0 16 16"><path d="M2 8.5l4 4 8-9" fill="none" stroke="#22b07d" stroke-width="2.4"/></svg>We keep up with everchanging cloud based technology</li>
    </ul>
  </div>
  <div class="abs why-shape"></div>
  <div class="abs why-photo" role="img" aria-label="Stack of tax folders and forms beside a calculator"></div>
</section>

<section>
  <div class="abs reviews"></div>
  <div class="abs hand" role="img" aria-label="Hand making an OK gesture"></div>
  <div class="abs reviews-title">Don't take<br><span>our word</span><br>for it</div>

  <div class="abs arrow" style="left:26px;top:2400px"><svg width="16" height="26" viewBox="0 0 16 26"><path d="M14 2 3 13l11 11" fill="none" stroke="#22b07d" stroke-width="4"/></svg></div>
  <div class="abs arrow" style="left:1140px;top:2400px"><svg width="16" height="26" viewBox="0 0 16 26"><path d="M2 2l11 11L2 24" fill="none" stroke="#22b07d" stroke-width="4"/></svg></div>

  <div class="abs review" style="left:110px"><div class="avatar" role="img" aria-label="Client portrait"></div><span class="quote" style="left:20px;top:20px">“</span><p>There are many variations of passages of Lorem Ipsum available, but the majority have suffered...</p><div class="who">- John Doe<br>Businessman</div><span class="quote" style="right:20px;bottom:20px">”</span></div>
  <div class="abs review" style="left:450px"><div class="avatar" role="img" aria-label="Client portrait"></div><span class="quote" style="left:20px;top:20px">“</span><p>There are many variations of passages of Lorem Ipsum available, but the majority have suffered...</p><div class="who">- John Doe<br>Businessman</div><span class="quote" style="right:20px;bottom:20px">”</span></div>
  <div class="abs review" style="left:790px"><div class="avatar" role="img" aria-label="Client portrait"></div><span class="quote" style="left:20px;top:20px">“</span><p>There are many variations of passages of Lorem Ipsum available, but the majority have suffered...</p><div class="who">- John Doe<br>Businessman</div><span class="quote" style="right:20px;bottom:20px">”</span></div>
</section>

<section>
  <h2 class="abs ind-title">Industries We Present</h2>
  <div class="abs ind" style="left:110px"><div class="num">01</div><div class="pic" role="img" aria-label="Doctor with a stethoscope" style="background:linear-gradient(135deg,#e6eef0,#b9ccd3)"></div><h3>Healthcare Specialists</h3><p>There are many variations of passages of Lorem Ipsum available, but the majority have suffered alteration in some form.</p></div>
  <div class="abs ind" style="left:450px"><div class="num">02</div><div class="pic" role="img" aria-label="Model house held in hands" style="background:linear-gradient(135deg,#e9ddd0,#a88a6e)"></div><h3>Contractors</h3><p>There are many variations of passages of Lorem Ipsum available, but the majority have suffered alteration in some form.</p></div>
  <div class="abs ind" style="left:790px"><div class="num">03</div><div class="pic" role="img" aria-label="Industrial machining equipment" style="background:linear-gradient(135deg,#9fb0bb,#4c5a63)"></div><h3>Manufacturing</h3><p>There are many variations of passages of Lorem Ipsum available, but the majority have suffered alteration in some form.</p></div>
  <div class="abs pager"><span class="on">1</span><span>2</span><span>3</span></div>
</section>

<footer>
  <div class="abs footer">
    <div class="abs f-brand"><div class="brand-dot"></div><div class="brand-name" style="color:#fff">LEDGERLINE<br>TAX ADVISORY</div></div>
    <p class="abs f-about">There are many variations of passages of Lorem Ipsum available, but the majority have suffered alteration in some form, by injected humour, or randomised words which.</p>
    <div class="abs f-social"></div>

    <div class="abs f-col" style="left:390px;top:80px"><h4>Quick Link</h4><ul><li>Home</li><li>Solution</li><li>Clients</li><li>Client Resources</li><li>Contact Us</li></ul></div>
    <div class="abs f-col" style="left:530px;top:80px;width:210px"><h4>Quick Contact</h4><ul>
      <li><span class="f-ico"></span>P.O Box 5520, Riverside,<br>Harbourview 4410</li>
      <li><span class="f-ico"></span>021 555 0187</li>
      <li><span class="f-ico"></span>+64 9 555 0142</li>
      <li><span class="f-ico"></span>hello@ledgerlinetax.example</li></ul></div>
    <div class="abs f-col" style="left:760px;top:80px;width:380px"><h4>Industries</h4>
      <ul style="float:left;width:190px"><li><span class="bullet"></span>Healthcare Specialists</li><li><span class="bullet"></span>Contractors</li><li><span class="bullet"></span>Manufacturing</li><li><span class="bullet"></span>Construction</li><li><span class="bullet"></span>Architecture</li><li><span class="bullet"></span>Real Estate Rentals</li></ul>
      <ul style="float:left;width:180px"><li><span class="bullet"></span>Legal</li><li><span class="bullet"></span>Medical Practices</li><li><span class="bullet"></span>Film Industry</li><li><span class="bullet"></span>Professional Services</li><li><span class="bullet"></span>Retail</li><li><span class="bullet"></span>Childcare</li></ul>
    </div>
  </div>
  <div class="abs copy">Copyright © 2022 ledgerlinetax.example All right reserved</div>
  <div class="abs to-top"><svg width="16" height="12" viewBox="0 0 16 12"><path d="M2 10l6-7 6 7" fill="none" stroke="#fff" stroke-width="2.6"/></svg></div>
</footer>

</body>
</html>
```